B.L.W.T. Business Card Design

we need a business card design for a motor vehicle repair business in Southport Australia, called Dravo's Automotive Repair Services. Our services include panel & paint, resprays and light bodyworks. We have a logo which we would like to use on the business card. We would like to see designs that use the colours blue and grey.

Industry/Entity Type

Automotive

Contact Information for Business Card

Dravo's Automotive Repair Services,
Merrin Folke,
7/2-5 Tralby Street Southport 4215, 0468 732 180, /dravosautomotiverepairservices, dravosautomotiverepairservices@quellmail.example,
services: panel & paint, respray, light bodyworks.
ABN: 47 206 519 782

Requirements
Must have
• Front of card must include attached logo and contact details.
please list services
Your eye should be drawn to the name (Merrin Folke) and phone number (0468 732 180).
Font must be legible and contemporary.
back of business card should have the following:
1. title - quote and
2. list the following: for, date, valid till, quote details and
3. a footer "to book you repair, please contact Merrin Folke on 0468 732 180".
There needs to be enough space to hand write details.
Should not have
• do not include any graphics/illustrations.

```html
<!DOCTYPE html>
<html lang="en">
<head>
<meta charset="utf-8">
<title>Dravo's Automotive Repair Services – Business Card</title>
<link rel="stylesheet" href="https://fonts.googleapis.com/css2?family=Abel&family=Open+Sans:wght@400;600&display=swap">
<style>
  :root {
    --page: #e9eaec;
    --grey: #5e5f61;
    --grey-dark: #4a4b4d;
    --grey-light: #7a7b7d;
    --blue: #0e5ea3;
    --blue-bright: #1f7fc6;
    --blue-soft: #3a8ccd;
    --white: #ffffff;
    --ink: #1c1c1c;
  }
  * { box-sizing: border-box; margin: 0; padding: 0; }
  html, body { width: 1200px; height: 1200px; overflow: hidden; }
  body {
    background: var(--page);
    position: relative;
    font-family: "Open Sans", sans-serif;
  }
  .card {
    position: absolute;
    left: 150px;
    width: 900px;
    height: 515px;
    background: var(--white);
    overflow: hidden;
    box-shadow: 0 6px 18px rgba(0,0,0,0.18);
  }
  .card--front { top: 60px; }
  .card--back { top: 625px; }

  .front-shapes { position: absolute; inset: 0; }

  .brand {
    position: absolute;
    left: 70px;
    top: 165px;
    display: flex;
    align-items: center;
    gap: 16px;
  }
  .brand__dot {
    width: 30px; height: 30px;
    border-radius: 50%;
    background: var(--blue);
    flex: none;
  }
  .brand__name {
    font-family: "Abel", sans-serif;
    font-size: 34px;
    color: var(--blue);
    line-height: 1.1;
    width: 380px;
  }

  .holder {
    position: absolute;
    right: 50px;
    top: 228px;
    font-family: "Abel", sans-serif;
    font-size: 44px;
    color: var(--blue);
    letter-spacing: 0.5px;
  }

  .contact {
    position: absolute;
    left: 70px;
    top: 348px;
    list-style: none;
    color: var(--white);
  }
  .contact__row {
    display: flex;
    align-items: center;
    gap: 14px;
    margin-bottom: 12px;
    font-size: 20px;
  }
  .contact__key {
    width: 24px; height: 24px;
    background: var(--grey-dark);
    color: var(--white);
    font-size: 14px;
    font-weight: 600;
    display: flex; align-items: center; justify-content: center;
    flex: none;
  }
  .contact__row--phone { font-size: 30px; }
  .contact__row--email { font-size: 19px; }

  .services {
    position: absolute;
    right: 45px;
    top: 345px;
    list-style: none;
    text-align: right;
    color: var(--white);
    font-weight: 600;
    font-size: 23px;
    line-height: 1.4;
  }

  .back-header {
    height: 120px;
    background: linear-gradient(90deg, var(--blue) 0%, var(--blue-bright) 60%, var(--blue-soft) 100%);
    display: flex; align-items: center; justify-content: center;
  }
  .back-header__title {
    font-family: "Abel", sans-serif;
    font-size: 44px;
    font-weight: 400;
    color: var(--white);
    letter-spacing: 0.5px;
  }
  .quote-fields {
    list-style: none;
    margin: 42px 0 0 115px;
    font-family: "Abel", sans-serif;
    font-size: 25px;
    color: var(--ink);
  }
  .quote-fields__row {
    display: flex;
    height: 45px;
    align-items: center;
  }
  .quote-fields__label { width: 165px; }
  .back-footer {
    position: absolute;
    left: 0; right: 0; bottom: 0;
    height: 92px;
    background: var(--grey);
    display: flex; align-items: center; justify-content: center;
    font-family: "Abel", sans-serif;
    font-size: 25px;
    color: var(--white);
  }
</style>
</head>
<body>

<section class="card card--front" aria-label="Business card front">
  <svg class="front-shapes" width="900" height="515" viewBox="0 0 900 515" aria-hidden="true">
    <rect x="0" y="0" width="900" height="85" fill="var(--grey-light)"/>
    <polygon points="730,0 900,0 900,85 700,85" fill="var(--blue-bright)"/>
    <rect x="0" y="300" width="900" height="215" fill="var(--grey)"/>
    <polygon points="650,300 900,300 900,515 595,515" fill="var(--blue)"/>
  </svg>

  <div class="brand">
    <span class="brand__dot"></span>
    <span class="brand__name">Dravo's Automotive Repair Services</span>
  </div>

  <h1 class="holder">Merrin Folke</h1>

  <ul class="contact">
    <li class="contact__row"><span class="contact__key">A</span>7/2-5 Tralby Street Southport 4215</li>
    <li class="contact__row contact__row--phone"><span class="contact__key">P</span>0468 732 180</li>
    <li class="contact__row contact__row--email"><span class="contact__key">E</span>dravosautomotiverepairservices@quellmail.example</li>
  </ul>

  <ul class="services">
    <li>panel &amp; paint</li>
    <li>respray</li>
    <li>light bodyworks</li>
  </ul>
</section>

<section class="card card--back" aria-label="Business card back">
  <header class="back-header">
    <h2 class="back-header__title">Dravo's Automotive Repair Services</h2>
  </header>
  <ul class="quote-fields">
    <li class="quote-fields__row"><span class="quote-fields__label">For</span>:</li>
    <li class="quote-fields__row"><span class="quote-fields__label">Date</span>:</li>
    <li class="quote-fields__row"><span class="quote-fields__label">Valid till</span>:</li>
    <li class="quote-fields__row"><span class="quote-fields__label">Quote details</span>:</li>
  </ul>
  <footer class="back-footer">to book you repair, please contact Merrin Folke on 0468 732 180</footer>
</section>

</body>
</html>
```